Marigold Works Flyer - RV Solar and Residential Solar

We would like to create a tri-fold brochure for our company for distribution in the mail. This will advertise our services, products and some references.

Our cover page should include a logo and contact information as well as some solar stock imagery.

Our inside pages should cover residential solar, RV solar and a solar education / facts portion.

The rear pages would be left for our remaining services and some references / testimonials.

Target Market(s)

Residential Homeowners and Recreational Vehicles

Industry/Entity Type

Solar Energy

Font styles to use
Serif
Sans Serif

Requirements
Must have
• Must match the color scheme of our logo.
Nice to have
• Solar stock images for RV solar and residential solar.
Either a black or white background with our logo is eye-catching,

```html
<!DOCTYPE html>
<html lang="en">
<head>
<meta charset="utf-8">
<title>Marigold Works Tri-Fold Brochure</title>
<link href="https://fonts.googleapis.com/css2?family=Montserrat:wght@400;500;600;700;800&display=swap" rel="stylesheet">
<style>
:root{
  --page:#e4e4e4;
  --ink:#111214;
  --green:#6cc04a;
  --green-dark:#4f9a32;
  --blue:#3d4fa8;
  --blue-deep:#2b3d8f;
  --cyan:#3bb6e8;
  --light:#e8eaec;
  --white:#ffffff;
}
*{box-sizing:border-box;margin:0;padding:0}
html,body{width:1200px;height:900px;overflow:hidden}
body{background:var(--page);font-family:"Montserrat",sans-serif;position:relative}
.spread{position:absolute;top:255px;width:575px;height:400px;box-shadow:0 8px 24px rgba(0,0,0,.18)}
.spread--outside{left:15px}
.spread--inside{left:610px}
.block{position:absolute;overflow:hidden}
.photo{position:absolute}
.brand{font-weight:700;color:var(--blue);letter-spacing:.5px;text-align:center}
.brand-dot{display:inline-block;width:8px;height:8px;border-radius:50%;background:var(--cyan);margin-right:5px;vertical-align:middle}

/* outside spread */
.services{left:0;top:95px;width:192px;height:180px;background:var(--ink);padding:14px 10px}
.services h2{color:var(--green);font-weight:600;font-size:14px;margin-bottom:8px}
.services ul{list-style:none}
.services li{color:var(--cyan);font-size:9.5px;font-weight:500;margin-bottom:8px}
.services li::before{content:"•";margin-right:5px}
.packages{left:192px;top:95px;width:192px;height:185px;background:var(--light);text-align:center;padding-top:50px}
.packages .brand{font-size:15px;margin-bottom:30px}
.packages p{color:var(--blue);font-weight:800;font-size:9.5px;line-height:15px}
.footer-dark{left:192px;top:372px;width:192px;height:28px;background:var(--ink);text-align:center;font-size:6px;line-height:8px;padding-top:3px;color:var(--white);font-weight:600}
.footer-dark .accent{color:var(--green)}
.cover-logo{left:384px;top:0;width:191px;height:95px;background:var(--ink);display:flex;align-items:center;justify-content:center}
.cover-logo .brand{font-size:16px}
.guarantee{left:384px;top:290px;width:191px;height:82px;background:var(--ink);text-align:center;padding-top:8px;line-height:1}
.guarantee .big{color:var(--green);font-weight:700;font-size:22px}
.guarantee .thin{color:var(--cyan);font-weight:400;font-size:12px}
.guarantee .white{color:var(--white);font-weight:800;font-size:18px}
.footer-green{top:372px;height:28px;background:var(--green);text-align:center;font-size:6px;line-height:8px;padding-top:3px;color:var(--ink);font-weight:700}

/* inside spread */
.rooftop{left:0;top:95px;width:192px;height:305px;background:linear-gradient(180deg,var(--blue-deep),var(--blue));padding:6px 10px}
.rooftop h2{color:var(--white);font-weight:500;font-size:15px;line-height:.95;text-align:center;margin-bottom:4px}
.rooftop h2 span{font-size:19px;font-weight:600}
.bullets{list-style:none}
.rooftop li{color:var(--white);font-size:5.3px;line-height:6.3px;margin-bottom:4.4px;padding-left:8px;position:relative;text-transform:uppercase}
.rooftop li::before{content:"";position:absolute;left:0;top:1px;width:3px;height:3px;border-radius:50%;background:var(--green)}
.rv{left:192px;top:95px;width:191px;height:170px;background:var(--ink);text-align:center;padding-top:8px;color:var(--white);text-transform:uppercase}
.rv h2{color:var(--green);font-weight:700;font-size:20px;margin-bottom:5px}
.rv .label{font-size:6px;font-weight:700}
.rv .price{font-size:12px;font-weight:800;margin-bottom:4px}
.rv .feat{font-size:6px;font-weight:800;margin-top:7px;padding:0 16px;line-height:7px}
.facts-head{left:383px;top:0;width:192px;height:40px;background:var(--ink);display:flex;align-items:center;justify-content:center}
.facts-head h2{color:var(--green);font-weight:600;font-size:20px}
.facts{left:383px;top:40px;width:192px;height:245px;background:var(--green);padding:8px 10px}
.facts li{color:var(--ink);font-size:5.4px;line-height:6.3px;margin-bottom:6px;padding-left:7px;position:relative;text-transform:uppercase;font-weight:500}
.facts li::before{content:"";position:absolute;left:0;top:1.5px;width:3px;height:3px;border-radius:50%;background:var(--ink)}
</style>
</head>
<body>

<section class="spread spread--outside">
  <div class="photo" style="left:0;top:0;width:384px;height:95px;background:linear-gradient(135deg,#5f86b8,#9cb8d8 55%,#3c5a80)" role="img" aria-label="Installers in hard hats mounting solar panels"></div>
  <div class="block services">
    <h2>SERVICES OFFERED</h2>
    <ul>
      <li>Agricultural Pivot Power</li>
      <li>Oil and Gas Systems</li>
      <li>Energy Audits</li>
      <li>Battery Storage Systems</li>
      <li>Off Grid Designs for Cottages</li>
      <li>Lake Houses</li>
    </ul>
  </div>
  <div class="photo" style="left:0;top:275px;width:192px;height:125px;background:radial-gradient(circle at 50% 45%,#f4b32a 0,#8a5a12 22%,#111214 48%)" role="img" aria-label="Glowing light bulb on black"></div>
  <div class="block packages">
    <div class="brand"><span class="brand-dot"></span>MARIGOLD WORKS</div>
    <p>RV PACKAGES<br>RESIDENTIAL PACKAGES<br>COMMERCIAL PACKAGES<br>ENERGY AUDIT</p>
  </div>
  <div class="photo" style="left:192px;top:280px;width:192px;height:92px;background:linear-gradient(180deg,#c9d7e6,#5e8fc4 60%,#2f5f93)" role="img" aria-label="Glass building facade seen from below"></div>
  <div class="block footer-dark">
    <div class="accent">PINE HOLLOW, ALBERTA, CANADA</div>
    <div>SALES@MARIGOLDWORKS.COM</div>
    <div class="accent">555.018.7731 OR 555.014.2290</div>
  </div>
  <div class="block cover-logo"><div class="brand"><span class="brand-dot"></span>MARIGOLD WORKS</div></div>
  <div class="photo" style="left:384px;top:95px;width:191px;height:97px;background:linear-gradient(135deg,#9cc1e8,#3e6fa8 60%,#1d2c44)" role="img" aria-label="Silhouette of an engineer with a tablet beside solar panels"></div>
  <div class="photo" style="left:384px;top:195px;width:94px;height:92px;background:linear-gradient(180deg,#b9d3ec,#6f8fae 55%,#6c9a3c)" role="img" aria-label="Solar field with wind turbines"></div>
  <div class="photo" style="left:481px;top:195px;width:94px;height:92px;background:radial-gradient(circle at 50% 50%,#d8e86a 0,#4f8a2c 40%,#28501a)" role="img" aria-label="Light bulb resting on green leaves"></div>
  <div class="block guarantee">
    <div class="big">LOWEST</div>
    <div class="thin">INSTALLED</div>
    <div class="white">SOLAR PRICE</div>
    <div class="thin">GUARANTEED</div>
  </div>
  <div class="block footer-green" style="left:384px;width:191px">
    <div>SALES@MARIGOLDWORKS.COM</div>
    <div>555-014-2290 OR 555-018-7731</div>
    <div>WWW.MARIGOLDWORKS.COM</div>
  </div>
</section>

<section class="spread spread--inside">
  <div class="photo" style="left:0;top:0;width:383px;height:95px;background:linear-gradient(180deg,#8fb3dc,#37578a 50%,#b4532c)" role="img" aria-label="Solar panels on a red tile roof"></div>
  <div class="block rooftop">
    <h2>RESIDENTIAL<br><span>ROOFTOP PV</span></h2>
    <ul class="bullets">
      <li>System sizes from 2.4kW to 12kW</li>
      <li>DIY packages available</li>
      <li>Referral bonus - 250$ for any successful solar referral</li>
      <li>Offset some or all of your energy use</li>
      <li>Electric vehicle charging systems</li>
      <li>Fully insured</li>
      <li>25 year system life</li>
      <li>Can raise value of your home by up to $20,000</li>
      <li>Extends the life of your roof</li>
      <li>100$ donation to a local charity as part of any solar install</li>
      <li>One free solar panel if ordered within one week of your birthday</li>
      <li>We offer financing. Finance a solar system with 20% down and you will be saving money immediately. Transfer the loan to your mortgage and increase your savings.</li>
      <li>Selling your house and love your solar? We will relocate the system to your new home for a small fee.</li>
    </ul>
  </div>
  <div class="block rv">
    <h2>RV SOLAR</h2>
    <div class="label">DIY 300W package from</div>
    <div class="price">500$</div>
    <div class="label">600W package from</div>
    <div class="price">700$</div>
    <div class="feat">Installation services available</div>
    <div class="feat">Keeps your batteries charged</div>
    <div class="feat">No longer deal with dead batteries</div>
    <div class="feat">Become the envy of all campers!</div>
    <div class="feat">Never have a dead cell phone battery again</div>
  </div>
  <div class="photo" style="left:192px;top:265px;width:191px;height:107px;background:linear-gradient(180deg,#2b3848,#1c2430 60%,#3b2a1c)" role="img" aria-label="RV parked among pine trees at dusk"></div>
  <div class="block footer-green" style="left:192px;width:191px">
    <div>SALES@MARIGOLDWORKS.COM</div>
    <div>555-014-2290 OR 555-018-7731</div>
    <div>WWW.MARIGOLDWORKS.COM</div>
  </div>
  <div class="block facts-head"><h2>SOLAR 101</h2></div>
  <div class="block facts">
    <ul class="bullets">
      <li>Alberta is the sunniest province in Canada and comparable to Florida</li>
      <li>Systems are designed to last 25 years but operate for as long as 40 years</li>
      <li>Virtually no maintenance required!</li>
      <li>How your power bill works.</li>
      <li>Protect yourself from rising power costs</li>
      <li>Not everyone can have solar. Once 30-40% of the market has solar, utilities will not allow all solar systems to be installed.</li>
      <li>Dispel the snow myth: snow only reduces a systems output by 5-8% over the course of a year. This is because our sunny hours are mostly made up in the longer summer days.</li>
      <li>Solar panels are nearly indestructible. Hail cannot damage a solar panel.</li>
      <li>Any extra power generated in the summer is sold back to the grid as a credit on your bill.</li>
    </ul>
  </div>
  <div class="photo" style="left:383px;top:285px;width:192px;height:115px;background:linear-gradient(180deg,#a9c9e6,#4a6e98 55%,#6f9c3a)" role="img" aria-label="Solar field with wind turbines on green grass"></div>
</section>

</body>
</html>
```